Help me create an amazing cover for my first ebook!!

I am looking to have a modern and professional looking cover for my first ebook. It will be published through Borvel Lumen Self Press and will need to follow their formatting and guidelines. I want the cover to have a modern and vibrant feel, that appeals to a millennial audience. This is a real estate book that is focused on a niche category catered to young professionals, so the idea would be to appeal to them.

Title:
The Zoomer Primer on Duplex Sharing

The Smartest Property Buying Plan to Start Early, Pay No Rent (or Almost None), and Rocket Boost Your Road to Money Independence.

Dane Wolsky

Target Market(s)

Real Estate investors, investors, millennials, young professionals, college educated, 20-40 years old.Financial freedom, finance.

Industry/Entity Type

Real Estate

Font styles to use
Sans Serif

Colors

Designer to choose colors to be used in the design.

Requirements
Must have
• Must follow the borvel lumen self press format. I attached a screenshot of the details, it can also be found here: https://lsp.borvel.example/en_US/help/topic/Q731920584
• Must include this title:
• The Zoomer Primer on Duplex Sharing
• The Smartest Property Buying Plan to Start Early, Pay No Rent (or Almost None), and Rocket Boost Your Road to Money Independence.
• Dane Wolsky.
• I added examples of book covers I like to use as a guide, I also added some color pallette examples.
Nice to have
• Modern, clean design that's not too busy. Some sort of simple photo or illustration to incorporate in the cover along with the text would be nice.

```html
<!DOCTYPE html>
<html lang="en">
<head>
<meta charset="utf-8">
<title>The Zoomer Primer on Duplex Sharing — Dane Wolsky</title>
<link rel="stylesheet" href="https://fonts.googleapis.com/css2?family=Bebas+Neue&family=Oswald:wght@300;400&display=swap">
<style>
  :root {
    --cover-navy: #1f4459;
    --title-blue: #0e9ee0;
    --title-red: #b3101b;
    --title-white: #ffffff;
    --rule-orange: #d98a1a;
    --art-wood: #c98d4e;
    --art-roof: #7a4a2c;
    --art-fence: #f2f2f2;
  }
  html, body {
    margin: 0;
    padding: 0;
    overflow: hidden;
    background: var(--cover-navy);
  }
  .cover {
    position: relative;
    width: 852px;
    height: 1200px;
    overflow: hidden;
    background: var(--cover-navy);
    font-family: "Bebas Neue", "Arial Narrow", sans-serif;
  }
  .title-the {
    position: absolute;
    left: 86px;
    top: 70px;
    margin: 0;
    font-size: 210px;
    line-height: 1;
    color: var(--title-blue);
    letter-spacing: 2px;
  }
  .title-main {
    position: absolute;
    left: 372px;
    top: 150px;
    margin: 0;
    color: var(--title-white);
    line-height: 0.9;
    font-weight: 400;
  }
  .title-main span { display: block; }
  .title-line-small { font-size: 90px; letter-spacing: 1px; }
  .title-line-on { font-size: 160px; margin-top: 4px; }
  .title-line-accent { font-size: 178px; color: var(--title-red); }
  .title-line-last { font-size: 168px; letter-spacing: 2px; }
  .house-art {
    position: absolute;
    left: 41px;
    top: 445px;
    width: 310px;
    height: 310px;
  }
  .divider {
    position: absolute;
    left: 0;
    top: 761px;
    width: 852px;
    height: 3px;
    background: var(--rule-orange);
  }
  .subtitle {
    position: absolute;
    left: 130px;
    top: 792px;
    width: 640px;
    margin: 0;
    font-family: "Oswald", "Arial Narrow", sans-serif;
    font-weight: 300;
    font-size: 31px;
    line-height: 44px;
    text-align: center;
    color: var(--title-white);
  }
  .subtitle .accent { color: var(--title-red); font-weight: 400; }
  .author {
    position: absolute;
    left: 0;
    top: 1100px;
    width: 900px;
    margin: 0;
    text-align: center;
    font-size: 64px;
    line-height: 1;
    color: var(--title-blue);
    letter-spacing: 1px;
  }
</style>
</head>
<body>
  <main class="cover">
    <h1 class="title-the">THE</h1>
    <h2 class="title-main">
      <span class="title-line-small">ZOOMER PRIMER</span>
      <span class="title-line-on">ON</span>
      <span class="title-line-accent">DUPLEX</span>
      <span class="title-line-last">SHARING</span>
    </h2>
    <svg class="house-art" viewBox="0 0 310 310" role="img" aria-label="Illustration of a small wooden log house with a chimney, round attic window and white picket fence">
      <defs>
        <linearGradient id="house-tone" x1="0" y1="0" x2="0" y2="1">
          <stop offset="0" stop-color="var(--art-roof)"/>
          <stop offset="0.35" stop-color="var(--art-wood)"/>
          <stop offset="0.85" stop-color="var(--art-wood)"/>
          <stop offset="1" stop-color="var(--art-fence)"/>
        </linearGradient>
      </defs>
      <rect x="0" y="0" width="310" height="310" fill="url(#house-tone)"/>
    </svg>
    <div class="divider"></div>
    <p class="subtitle">The <span class="accent">Smartest</span> Property Buying Plan to Start Early, Pay No Rent (or Almost None), and Rocket Boost Your Road to Money Independence.</p>
    <p class="author">DANE WOLSKY.</p>
  </main>
</body>
</html>
```